Request for Business Card Design

Hi. My name is Marlena, I am looking for a new business card design for my company, Quillbrook Sensing Systems, LLC. I really like the design you did for Tavel Harvest and was hoping you could do something similar using our full logo and our mark. I am also open to any raised texture design using our mark. I have attached our full logo, which would need to be somewhere on the card, as well as the mark in both outline and full form, as well as our brand colors / guide. The card does not have to be white, as long as our logo and mark appear. I actually like darker colored business cards more, but am open to all options. If you are interested in working with me, please let me know. We would also take the business card design into letterhead design if you can do that.

```html
<!DOCTYPE html>
<html lang="en">
<head>
<meta charset="utf-8">
<title>Quillbrook Sensing Systems – Business Card</title>
<link rel="stylesheet" href="https://fonts.googleapis.com/css2?family=Montserrat:wght@400;500;600;700&display=swap">
<style>
  :root {
    --brand-blue: #1c9dc1;
    --brand-tint: #e3f1f6;
    --ink: #1c1c1c;
    --ink-soft: #3a3a3a;
    --card: #ffffff;
    --backdrop: #e8ebee;
  }
  * { box-sizing: border-box; margin: 0; padding: 0; }
  html, body {
    width: 1198px; height: 1200px; overflow: hidden;
    background: var(--backdrop);
    font-family: "Montserrat", Arial, sans-serif;
    color: var(--ink);
  }
  .card {
    position: absolute; left: 167px;
    width: 865px; height: 509px;
    background: var(--card);
    overflow: hidden;
  }
  .card--front { top: 74px; }
  .card--back { top: 621px; }

  .company-band {
    position: absolute; left: 0; top: 49px;
    width: 792px; height: 110px;
    background: var(--brand-blue);
    border-radius: 0 0 140px 0 / 0 0 110px 0;
    color: #fff;
    padding: 22px 0 0 71px;
  }
  .company-band__name {
    font-weight: 700; font-size: 23px; letter-spacing: 0.6px;
    text-transform: uppercase;
  }
  .company-band__address {
    display: flex; align-items: center; gap: 20px;
    margin-top: 10px; font-size: 21px; font-weight: 400; letter-spacing: 0.3px;
  }
  .company-band__address svg { width: 16px; height: 18px; fill: #fff; margin-left: 2px; }

  .wordmark {
    position: absolute; display: flex; align-items: center; gap: 16px;
    color: var(--ink-soft);
  }
  .wordmark__dot {
    width: 52px; height: 52px; border-radius: 50%;
    background: var(--brand-blue);
  }
  .wordmark__name {
    font-weight: 600; font-size: 44px; letter-spacing: 3px;
  }
  .card--front .wordmark { left: 71px; top: 243px; }

  .holder-name {
    position: absolute; right: 63px; top: 244px;
    font-weight: 700; font-size: 29px; letter-spacing: 1px;
    text-transform: uppercase;
  }
  .contact-list {
    position: absolute; right: 63px; top: 316px;
    list-style: none; text-align: right;
  }
  .contact-list li {
    display: flex; justify-content: flex-end; align-items: center; gap: 14px;
    font-size: 22px; font-weight: 500; height: 33px; letter-spacing: 0.3px;
  }
  .contact-list svg { width: 17px; height: 17px; fill: var(--ink); flex: none; }

  .decor-circle {
    position: absolute; left: 232px; top: 33px;
    width: 640px; height: 640px; border-radius: 50%;
    background: var(--brand-tint);
  }
  .card--back .wordmark { left: 258px; top: 217px; }
</style>
</head>
<body>

<section class="card card--front">
  <header class="company-band">
    <h1 class="company-band__name">Quillbrook Sensing Systems, LLC</h1>
    <p class="company-band__address">
      <svg viewBox="0 0 16 18" aria-hidden="true"><path d="M8 0a5.5 5.5 0 0 0-5.5 5.5C2.5 9.6 8 14 8 14s5.5-4.4 5.5-8.5A5.5 5.5 0 0 0 8 0zm0 7.6A2.1 2.1 0 1 1 8 3.4a2.1 2.1 0 0 1 0 4.2zM1 15.5h14V17H1z"/></svg>
      58 Harlow Ave, Suite 210, Ashbury MA 02391
    </p>
  </header>

  <div class="wordmark">
    <span class="wordmark__dot"></span>
    <span class="wordmark__name">QUILLBROOK</span>
  </div>

  <h2 class="holder-name">Marlena</h2>
  <ul class="contact-list">
    <li>617-555-0142
      <svg viewBox="0 0 24 24" aria-hidden="true"><path d="M6.6 10.8a15.1 15.1 0 0 0 6.6 6.6l2.2-2.2a1 1 0 0 1 1-.25 11.4 11.4 0 0 0 3.6.57 1 1 0 0 1 1 1V20a1 1 0 0 1-1 1A17 17 0 0 1 3 4a1 1 0 0 1 1-1h3.5a1 1 0 0 1 1 1c0 1.25.2 2.45.57 3.57a1 1 0 0 1-.25 1z"/></svg>
    </li>
    <li>617-555-0187
      <svg viewBox="0 0 24 24" aria-hidden="true"><path d="M6 2h12v5H6zM3 8h18a2 2 0 0 1 2 2v7h-4v5H5v-5H1v-7a2 2 0 0 1 2-2zm4 8v4h10v-4z"/></svg>
    </li>
    <li>info@quillbrook.com
      <svg viewBox="0 0 24 24" aria-hidden="true"><path d="M2 5h20v14H2zm2 2v.5l8 5 8-5V7l-8 5z"/></svg>
    </li>
    <li>www.quillbrook.com
      <svg viewBox="0 0 24 24" aria-hidden="true"><path d="M12 2a10 10 0 1 0 0 20 10 10 0 0 0 0-20zm6.9 6h-3a15.6 15.6 0 0 0-1.3-3.6A8 8 0 0 1 18.9 8zM12 4c.8 1.2 1.5 2.5 1.9 4h-3.8c.4-1.5 1.1-2.8 1.9-4zM4.3 14a8 8 0 0 1 0-4h3.4a16 16 0 0 0 0 4zm.8 2h3a15.6 15.6 0 0 0 1.3 3.6A8 8 0 0 1 5.1 16zm3-8h-3a8 8 0 0 1 4.3-3.6A15.6 15.6 0 0 0 8.1 8zM12 20c-.8-1.2-1.5-2.5-1.9-4h3.8c-.4 1.5-1.1 2.8-1.9 4zm2.3-6H9.7a14.6 14.6 0 0 1 0-4h4.6a14.6 14.6 0 0 1 0 4zm.3 5.6a15.6 15.6 0 0 0 1.3-3.6h3a8 8 0 0 1-4.3 3.6zm1.7-5.6a16 16 0 0 0 0-4h3.4a8 8 0 0 1 0 4z"/></svg>
    </li>
  </ul>
</section>

<section class="card card--back">
  <div class="decor-circle"></div>
  <div class="wordmark">
    <span class="wordmark__dot"></span>
    <span class="wordmark__name">QUILLBROOK</span>
  </div>
</section>

</body>
</html>
```